Landscape Contractor in need of New Web Design

HELP.. Please Help!!!!. Our current website is old, outdated, ugly... and well nothing like us.... so we are looking for someone to help build a new website that fits our company direction. We are a landscape company with multiple locations in order to meet the needs of our clients and their projects throughout the midwest. When most people think of landscaping, they think of mowing grandmas yard, but that is NOT even remotely close to what we do. We are 100% a commercial landscape company meaning we complete landscape and irrigation services for large scale commercial projects. We are looking for a website to showcase our commercial talents and awesome team of people.
Updates

Address of current website is www.plovermeadowco.com

```html
<!DOCTYPE html>
<html lang="en">
<head>
<meta charset="utf-8">
<title>Plover Meadow Co. – Commercial Landscape &amp; Irrigation</title>
<link href="https://fonts.googleapis.com/css2?family=Poppins:ital,wght@0,300;0,400;0,500;0,600;1,400;1,600&display=swap" rel="stylesheet">
<style>
:root{
  --forest:#07493c;
  --forest-deep:#063f34;
  --lime:#c6f200;
  --sage:#c2d3c0;
  --ink:#0b4a3d;
  --white:#ffffff;
}
*{box-sizing:border-box;margin:0;padding:0}
html,body{width:1200px;height:5085px;overflow:hidden}
body{position:relative;background:var(--white);font-family:"Poppins",sans-serif;color:var(--ink)}
.abs{position:absolute}

/* header & hero */
.hero-band{left:0;top:0;width:1200px;height:553px;background:var(--forest)}
.brand{display:flex;align-items:center;gap:12px;font-weight:600;color:var(--white);letter-spacing:.2px;white-space:nowrap}
.brand-dot{border-radius:50%;background:var(--lime);flex:none}
.header-brand{left:89px;top:22px;font-size:20px}
.header-brand .brand-dot{width:70px;height:70px}
.topline{right:90px;top:18px;font-size:16px;color:var(--white);display:flex;align-items:center;gap:10px}
.nav{left:320px;top:59px;display:flex;gap:42px;font-size:16px;color:var(--white)}
.nav .active{color:var(--lime)}
.btn-quote{left:965px;top:55px;width:146px;height:36px;border-radius:18px;background:var(--lime);color:var(--forest);font-size:15px;display:flex;align-items:center;justify-content:center}
.hero-photo{left:324px;top:112px;width:876px;height:506px;background:linear-gradient(160deg,#8d8f8a 0%,#7b7f75 35%,#4f7b38 65%,#3e6a2a 100%)}
.hero-title{left:178px;top:266px;color:var(--white);font-size:37px;font-weight:300;line-height:44px}
.hero-title b{font-weight:600;font-size:31px;display:block;line-height:38px}
.hero-ctrl{left:176px;top:444px;display:flex;align-items:center;gap:14px}
.hero-ctrl .line{width:290px;height:1px;background:var(--white)}
.scroll-mouse{left:588px;top:532px;width:24px;height:44px;border:2px solid var(--white);border-radius:12px}
.scroll-mouse::after{content:"";position:absolute;left:9px;top:8px;width:2px;height:6px;background:var(--white);border-radius:1px}

/* shared section heading */
.sec-title{font-size:33px;font-weight:300;left:174px}
.sec-rule{left:148px;width:174px;height:1px;background:var(--ink)}
.sec-lead{left:351px;width:660px;font-size:15px;line-height:22px}
.light{color:var(--white)}
.rule-light{background:var(--white)}

/* why choose us */
.feature{width:260px}
.feature svg{display:block;margin-bottom:16px}
.feature h3{font-size:17px;font-weight:500;margin-bottom:8px}
.feature p{font-size:12.5px;line-height:20px}
.dots{display:flex;gap:8px}
.dot{width:12px;height:12px;border:1.5px solid var(--ink);border-radius:50%}
.dot.on{background:radial-gradient(circle,var(--ink) 2px,transparent 3px)}

/* services */
.sage-band{left:0;top:1613px;width:1200px;height:1847px;background:var(--sage)}
.services-panel{left:59px;top:1218px;width:1082px;height:908px;background:var(--forest)}
.svc{width:263px}
.svc .img{width:263px;height:231px}
.svc h4{font-size:17px;font-weight:500;color:var(--white);margin-top:24px;line-height:22px}
.svc h4.hover{color:var(--lime)}

/* gallery */
.gal{position:absolute}
.gal-overlay{display:flex;flex-direction:column;align-items:center;justify-content:center;color:var(--lime);font-size:20px;gap:14px}
.lime-bar{left:586px;top:3533px;width:439px;height:12px;background:var(--lime)}
.btn-dark{left:351px;top:3377px;width:129px;height:36px;border-radius:18px;background:var(--forest);color:var(--white);font-size:14px;display:flex;align-items:center;justify-content:center}

/* testimonial */
.testimonial-band{left:0;top:3460px;width:1200px;height:577px;background:var(--forest)}
.quote-text{left:190px;top:3706px;width:820px;text-align:center;color:var(--white);font-style:italic;font-size:18px;line-height:28px}
.quote-name{left:0;width:1200px;text-align:center;color:var(--white);font-style:italic}

/* about */
.about-sage{left:89px;top:4009px;width:408px;height:549px;background:var(--sage)}
.about-card{left:116px;top:4037px;width:1084px;height:614px;background:var(--white)}
.about-title{left:174px;top:4080px;font-size:33px;font-weight:300;line-height:50px}
.about-title b{font-weight:500}
.about-text{left:176px;top:4276px;width:480px;font-size:15px;line-height:28px}
.btn-lime{left:176px;top:4479px;width:156px;height:38px;border-radius:19px;background:var(--lime);color:var(--forest);font-size:14px;display:flex;align-items:center;justify-content:center}

/* footer */
.footer{left:0;top:4651px;width:1200px;height:434px;background:var(--forest)}
.footer-brand{left:89px;top:4750px;font-size:20px}
.footer-brand .brand-dot{width:100px;height:100px}
.f-head{font-size:17px;font-weight:500;color:var(--white)}
.f-line{display:flex;align-items:center;gap:14px;color:var(--white);font-size:21px;font-weight:300}
.f-small{font-size:15px;font-weight:400}
.newsletter{left:700px;top:4854px;width:325px;height:44px;border-radius:22px;background:#3d6e62;display:flex;align-items:center;padding:0 8px 0 22px;color:#d7e3de;font-size:13px;justify-content:space-between}
.send{width:36px;height:36px;border-radius:50%;background:var(--lime);display:flex;align-items:center;justify-content:center}
.footer-rule{left:89px;top:5002px;width:1022px;height:1px;background:rgba(255,255,255,.35)}
.copyright{left:89px;top:5030px;font-size:13px;color:var(--white)}
.copyright span{color:var(--lime)}
.social{display:flex;gap:8px;left:977px;top:5020px}
.social i{width:40px;height:40px;border:1.5px solid var(--lime);border-radius:50%;display:block}
.social i.on{background:var(--lime)}
</style>
</head>
<body>

<!-- header & hero -->
<div class="abs hero-band"></div>
<div class="abs brand header-brand"><span class="brand-dot"></span>Plover Meadow</div>
<div class="abs topline">
  <svg width="16" height="16" viewBox="0 0 24 24" fill="none" stroke="#c6f200" stroke-width="2"><path d="M5 3h4l2 5-3 2a12 12 0 0 0 6 6l2-3 5 2v4a2 2 0 0 1-2 2A17 17 0 0 1 3 5a2 2 0 0 1 2-2z"/></svg>
  (913) 555-0142 &nbsp;/&nbsp; (785) 555-0187
</div>
<nav class="abs nav"><span class="active">Home</span><span>Divisions</span><span>Services</span><span>About Us</span><span>Gallery</span><span>Contact</span></nav>
<div class="abs btn-quote">Get a Quote</div>
<div class="abs hero-photo" role="img" aria-label="Commercial building with stone columns, lush lawn and flowering beds"></div>
<h1 class="abs hero-title">We have a passion in creating<b>new &amp; unique spaces</b></h1>
<div class="abs hero-ctrl">
  <svg width="40" height="20" viewBox="0 0 40 20" fill="none" stroke="#fff" stroke-width="2"><path d="M10 4 4 10l6 6M28 4l6 6-6 6"/></svg>
  <span class="line"></span>
</div>
<div class="abs scroll-mouse"></div>

<!-- why choose us -->
<h2 class="abs sec-title" style="top:700px">Why Choose Us?</h2>
<div class="abs sec-rule" style="top:780px"></div>
<p class="abs sec-lead" style="top:768px">Lorem ipsum dolor sit amet, consectetur adipiscing elit, sed do eiusmod tempor incididunt ut labore et dolore magna aliqua.</p>

<div class="abs feature" style="left:176px;top:862px">
  <svg width="60" height="60" viewBox="0 0 60 60" fill="#07493c"><path d="M14 8 4 30h20zM30 2 18 30h24zM46 8 36 30h20z"/><rect x="2" y="36" width="56" height="4"/><rect x="2" y="46" width="56" height="4"/><rect x="12" y="30" width="3" height="26"/><rect x="28.5" y="30" width="3" height="26"/><rect x="45" y="30" width="3" height="26"/></svg>
  <h3>Specialized Company</h3>
  <p>Plover Meadow strives to set the standard for the highest quality lawn and landscape products and services and to exceed our customer's expectations every time.</p>
</div>
<div class="abs feature" style="left:468px;top:862px">
  <svg width="60" height="60" viewBox="0 0 60 60" fill="none" stroke="#07493c" stroke-width="4"><path d="M30 4 8 12v16c0 14 10 24 22 28 12-4 22-14 22-28V12z" fill="#07493c"/><path d="M30 12 16 17v11c0 9 6 16 14 19 8-3 14-10 14-19V17z" stroke="#fff" stroke-width="2.5"/><path d="m22 30 6 6 11-12" stroke="#fff"/></svg>
  <h3>Licensed &amp; Insured</h3>
  <p>Rest assured knowing that Plover Meadow Co. is fully licensed and insured and has a superior safety rating.</p>
</div>
<div class="abs feature" style="left:762px;top:862px">
  <svg width="60" height="60" viewBox="0 0 60 60" fill="#07493c"><path d="M14 4c8 0 12 6 12 14-8 0-12-6-12-14zM34 10c-6 0-10 4-10 10 6 0 10-4 10-10z"/><rect x="22" y="16" width="4" height="22"/><path d="M6 38h34l-4 18H10z"/><path d="M40 40 56 26l3 3-15 15z"/></svg>
  <h3>Dependable Services</h3>
  <p>Communication is highly valued at Plover Meadow. From start to finish our clients will be kept up to date on their project.</p>
</div>
<div class="abs dots" style="left:582px;top:1101px"><span class="dot"></span><span class="dot on"></span></div>

<!-- services -->
<div class="abs sage-band"></div>
<section class="abs services-panel"></section>
<h2 class="abs sec-title light" style="top:1285px">Exceptional services we offer</h2>
<div class="abs sec-rule rule-light" style="top:1364px"></div>
<p class="abs sec-lead light" style="top:1352px">Lorem ipsum dolor sit amet, consectetur adipiscing elit, sed do eiusmod tempor incididunt ut labore et dolore magna aliqua.</p>

<div class="abs svc" style="left:176px;top:1439px"><div class="img" role="img" aria-label="Ride-on mower cutting a commercial lawn" style="background:linear-gradient(180deg,#6f8c5a,#4f8a2a)"></div><h4>Maintenance</h4></div>
<div class="abs svc" style="left:468px;top:1439px"><div class="img" role="img" aria-label="Technician spraying fertilizer among shrubs" style="background:linear-gradient(180deg,#7f9a5c,#4b6d35)"></div><h4 class="hover">Chemical Applications &amp;<br>Fertilization</h4></div>
<div class="abs svc" style="left:762px;top:1439px"><div class="img" role="img" aria-label="Healthy turf beside a planted garden bed" style="background:linear-gradient(180deg,#5a7a40,#6aa52c)"></div><h4>Turf Management</h4></div>
<div class="abs svc" style="left:176px;top:1771px"><div class="img" role="img" aria-label="Stone steps and paved plaza with landscaped beds" style="background:linear-gradient(180deg,#a9c0c9,#6d8a55 60%,#8c8a78)"></div><h4>Hardscaping</h4></div>
<div class="abs svc" style="left:468px;top:1771px"><div class="img" role="img" aria-label="Sprinklers watering a curved lawn" style="background:linear-gradient(180deg,#6a9a3a,#9bbf4a 60%,#8a6b55)"></div><h4>Irrigation</h4></div>
<div class="abs svc" style="left:762px;top:1771px"><div class="img" role="img" aria-label="Layered planting bed with hostas and flowers" style="background:linear-gradient(180deg,#6b5d5a,#5d8c3a)"></div><h4>Landscaping</h4></div>

<!-- gallery -->
<h2 class="abs sec-title" style="top:2207px">Photo Gallery</h2>
<div class="abs sec-rule" style="top:2288px"></div>
<p class="abs sec-lead" style="top:2276px">Lorem ipsum dolor sit amet, consectetur adipiscing elit, sed do eiusmod tempor incididunt ut labore et dolore magna aliqua.</p>

<div class="gal" role="img" aria-label="Stone entry sign surrounded by bright foliage" style="left:176px;top:2371px;width:438px;height:479px;background:linear-gradient(170deg,#6d8c56,#8eb43f 60%,#5d6a3c)"></div>
<div class="gal" role="img" aria-label="Building facade with lawn and flower border" style="left:586px;top:2426px;width:439px;height:369px;background:linear-gradient(170deg,#8a8580,#6e7d5e 50%,#3f6e2a)"></div>
<div class="gal gal-overlay" style="left:614px;top:2795px;width:411px;height:369px;background:linear-gradient(rgba(7,73,60,.88),rgba(7,73,60,.88)),#3f5a3e" role="img" aria-label="Commercial landscape project">
  <svg width="56" height="56" viewBox="0 0 56 56" stroke="#c6f200" stroke-width="2"><path d="M28 0v56M0 28h56"/></svg>
  Commercial
</div>
<div class="gal" role="img" aria-label="Flowering perennials with pink hibiscus" style="left:176px;top:2850px;width:438px;height:480px;background:linear-gradient(170deg,#a8b0a8,#6b8a3e 40%,#9e6b3a 75%,#c88aa0)"></div>
<div class="abs btn-dark">View All</div>

<!-- testimonial -->
<div class="abs testimonial-band"></div>
<div class="gal" role="img" aria-label="Daylilies in front of a residential building" style="left:586px;top:3164px;width:439px;height:369px;background:linear-gradient(170deg,#b6bfc0,#4d7a33 45%,#5d8c2e 70%,#9a4a3a)"></div>
<div class="abs lime-bar"></div>
<svg class="abs" style="left:560px;top:3620px" width="80" height="58" viewBox="0 0 80 58" fill="#c6f200"><path d="M0 30C0 12 10 2 26 0v10c-8 2-12 8-12 16h14v32H0zM42 30C42 12 52 2 68 0v10c-8 2-12 8-12 16h14v32H42z"/></svg>
<p class="abs quote-text">I have been working with Plover Meadow for several years. As a building/development firm I understand the importance of landscaping in our projects. Plover Meadow has provided expert landscape consultation and performance on all projects I have had the opportunity to work with them on.</p>
<p class="abs quote-name" style="top:3848px;font-weight:600;font-size:15px">Dennis R Whitford</p>
<p class="abs quote-name" style="top:3876px;font-size:15px">Whitford Construction Company</p>
<div class="abs dots" style="left:545px;top:3928px">
  <span class="dot" style="border-color:#c6f200"></span><span class="dot on" style="border-color:#c6f200;background:radial-gradient(circle,#c6f200 2px,transparent 3px)"></span><span class="dot" style="border-color:#c6f200"></span><span class="dot" style="border-color:#c6f200"></span><span class="dot" style="border-color:#c6f200"></span><span class="dot" style="border-color:#c6f200"></span>
</div>

<!-- about -->
<div class="abs about-sage"></div>
<div class="abs about-card"></div>
<h2 class="abs about-title"><b>Plover Meadow Co.</b> is a<br>Full Service Lawn and Landscape<br>Contractor</h2>
<div class="abs sec-rule" style="top:4242px"></div>
<p class="abs about-text">Founded by Evan Marsh and Adrian Holloway, Plover Meadow is the premier landscape maintenance and design company based in Westbrook, Kansas. Our company's dedication to innovative design projects created some of the most distinguished landscape projects throughout Kansas, Missouri, and Oklahoma.</p>
<div class="abs btn-lime">Discover More</div>
<svg class="abs" style="left:700px;top:4090px" width="415" height="411" viewBox="0 0 415 411" role="img" aria-label="Collage of landscaped lawns and garden paths in diamond frames">
  <defs>
    <linearGradient id="g1" x1="0" y1="0" x2="1" y2="1"><stop offset="0" stop-color="#8fbf3a"/><stop offset="1" stop-color="#4f8a2a"/></linearGradient>
    <linearGradient id="g2" x1="0" y1="0" x2="1" y2="1"><stop offset="0" stop-color="#6f9a3a"/><stop offset="1" stop-color="#b08a7a"/></linearGradient>
  </defs>
  <polygon points="176,0 290,112 176,224 62,112" fill="url(#g1)"/>
  <polygon points="306,128 415,237 306,346 197,237" fill="url(#g2)"/>
  <polygon points="118,175 236,293 118,411 0,293" fill="url(#g1)"/>
</svg>

<!-- footer -->
<footer class="abs footer"></footer>
<div class="abs brand footer-brand"><span class="brand-dot"></span>Plover Meadow</div>
<p class="abs f-head" style="left:350px;top:4740px">Contact Us</p>
<div class="abs f-line" style="left:350px;top:4776px"><svg width="18" height="18" viewBox="0 0 24 24" fill="none" stroke="#c6f200" stroke-width="2"><path d="M5 3h4l2 5-3 2a12 12 0 0 0 6 6l2-3 5 2v4a2 2 0 0 1-2 2A17 17 0 0 1 3 5a2 2 0 0 1 2-2z"/></svg>1-913-555-0142</div>
<div class="abs f-line" style="left:350px;top:4811px"><svg width="18" height="18" viewBox="0 0 24 24" fill="none" stroke="#c6f200" stroke-width="2"><path d="M5 3h4l2 5-3 2a12 12 0 0 0 6 6l2-3 5 2v4a2 2 0 0 1-2 2A17 17 0 0 1 3 5a2 2 0 0 1 2-2z"/></svg>1-785-555-0187</div>
<div class="abs f-line f-small" style="left:350px;top:4844px"><svg width="16" height="16" viewBox="0 0 24 24" fill="none" stroke="#c6f200" stroke-width="2"><rect x="3" y="6" width="18" height="13"/><path d="m3 6 9 7 9-7"/></svg><u>info@plovermeadowco.com</u></div>
<div class="abs f-line f-small" style="left:350px;top:4877px;align-items:flex-start"><svg width="16" height="18" viewBox="0 0 24 24" fill="none" stroke="#c6f200" stroke-width="2"><path d="M12 22s7-7 7-12a7 7 0 0 0-14 0c0 5 7 12 7 12z"/><circle cx="12" cy="10" r="2.5"/></svg><span>4410 W 97th Terrace Westbrook,<br>KS 66219</span></div>

<p class="abs f-head" style="left:700px;top:4740px">Sign Up Newsletter</p>
<p class="abs" style="left:700px;top:4777px;width:300px;font-size:14px;line-height:22px;color:var(--white)">Lorem ipsum dolor sit amet, sedtur consectetur adipiscing</p>
<div class="abs newsletter">Enter your email ...<span class="send"><svg width="16" height="16" viewBox="0 0 24 24" fill="none" stroke="#07493c" stroke-width="2"><path d="M3 4l18 8-18 8 3-8zM6 12h15"/></svg></span></div>
<svg class="abs" style="left:1098px;top:4742px" width="26" height="26" viewBox="0 0 26 26" fill="none" stroke="#c6f200" stroke-width="2"><path d="M4 22 13 3l9 19M8 14h10"/></svg>

<div class="abs footer-rule"></div>
<p class="abs copyright">© 2021 <span>Plover Meadow</span>. All Rights Reserved</p>
<div class="abs social" aria-label="Social links"><i></i><i class="on"></i><i></i></div>

</body>
</html>
```